Solids Control Presentation Template Design

I'm putting together a technical 5-day course about solids control and waste management. I'm looking for an updated art and a easy on the eyes format.

```html
<!DOCTYPE html>
<html lang="en">
<head>
<meta charset="utf-8">
<title>Solids Control and Waste Management – Presentation Template</title>
<link rel="stylesheet" href="https://fonts.googleapis.com/css2?family=Lato:wght@400;700;900&family=Arimo:wght@700&display=swap">
<style>
:root{
  --red:#a8262f;
  --red-bright:#d63a42;
  --pink:#d98e93;
  --ink:#2e2e2e;
  --grey:#707070;
  --grey-mid:#8e8e8e;
  --grey-light:#c9c9c9;
  --panel:#f1f1f1;
  --rule:#e3e3e3;
  --blue:#4b61a6;
  --page:#f7f7f7;
}
*{box-sizing:border-box}
html,body{margin:0;padding:0}
body{width:1200px;height:2201px;overflow:hidden;position:relative;background:var(--page);font-family:'Lato',sans-serif;color:var(--ink)}

/* hero title slide */
.hero{position:absolute;left:67px;top:44px;width:621px;height:350px;overflow:hidden;box-shadow:0 3px 10px rgba(0,0,0,.35)}
.hero-photo{position:absolute;inset:0;background:linear-gradient(180deg,#c7d0d6 0%,#dfe4e7 55%,#d2d6d6 100%)}
.hero-brand{position:absolute;left:288px;top:136px;width:290px;text-align:center}
.hero-brand .name{display:block;font-size:36px;font-weight:900;letter-spacing:2px;color:#262626;line-height:40px}
.hero-brand .services{display:block;margin-top:8px;font-size:8.5px;font-weight:700;letter-spacing:1.6px;color:#333}
.hero-title{position:absolute;left:296px;top:210px;margin:0;font-size:23px;line-height:23px;font-weight:900;color:var(--red-bright);letter-spacing:-.3px}

/* feature checklist */
.features{position:absolute;left:760px;top:32px;width:432px;margin:0;padding:0;list-style:none;font-family:'Arimo',sans-serif;font-weight:700;font-size:22px;line-height:27px;color:#1d1d1d}
.features>li{position:relative;padding-left:26px;margin-bottom:3px}
.features>li::before{content:"";position:absolute;left:2px;top:3px;width:17px;height:19px;border:2px solid #1d1d1d;border-left-width:3px;border-bottom-width:3px}
.features ul{list-style:none;margin:2px 0 0 50px;padding:0;font-size:19px;line-height:23px}
.features ul li{position:relative;padding-left:18px;margin-bottom:1px}
.features ul li::before{content:"";position:absolute;left:0;top:7px;width:7px;height:7px;background:#1d1d1d}

/* slide thumbnails */
.slide{position:absolute;width:370px;height:209px;background:#fff;overflow:hidden;box-shadow:0 2px 6px rgba(0,0,0,.35)}
.slide.shaded{background:var(--panel)}
.head{position:absolute;left:0;top:0;width:100%;height:34px;background:#fff;border-bottom:1px solid var(--rule)}
.title{position:absolute;left:24px;top:9px;margin:0;padding-left:8px;border-left:2px solid var(--ink);font-size:13px;line-height:16px;font-weight:700;color:var(--ink)}
.title em{font-style:normal;color:var(--red)}
.mark{position:absolute;right:28px;top:10px;text-align:center}
.mark b{display:block;font-size:8px;line-height:9px;font-weight:900;letter-spacing:.6px;color:var(--ink)}
.mark i{display:block;font-style:normal;font-size:2.6px;line-height:4px;color:var(--grey)}
.foot{position:absolute;left:26px;bottom:7px;font-size:4px;font-weight:900;color:var(--ink)}
.page-no{position:absolute;right:0;bottom:0;width:18px;height:18px;background:var(--red);clip-path:polygon(100% 0,100% 100%,0 100%)}
.page-no span{position:absolute;right:3px;bottom:3px;font-size:3.5px;color:#fff}

.txt{margin:0;font-size:4.6px;line-height:6.4px;color:var(--grey);text-align:justify}
.txt+.txt{margin-top:6px}
.photo{position:absolute}
.ph-sky{background:linear-gradient(180deg,#8ea4bf 0%,#c8cfd6 55%,#2a2a2a 100%)}
.ph-sunset{background:linear-gradient(180deg,#d6a25a 0%,#b97a2c 60%,#3a2a16 100%)}
.ph-plant{background:linear-gradient(180deg,#9aa3a5 0%,#4f8f8c 45%,#2f6a3a 100%)}
.ph-mud{background:linear-gradient(160deg,#9a8f80 0%,#6f6557 100%)}
.ph-crew{background:linear-gradient(160deg,#d9d9d6 0%,#7e6d55 100%)}
.ph-pit{background:linear-gradient(160deg,#8a5a3a 0%,#4a3224 100%)}
.ph-screen{background:linear-gradient(160deg,#c9c4ba 0%,#a59d90 100%)}
.ph-tower{background:linear-gradient(180deg,#d5d5d5 0%,#bdbdbd 100%)}

/* about */
.about-block{position:absolute;left:189px;top:54px;width:160px;padding-left:4px;border-left:1px solid var(--red)}
.about-block .kicker{display:block;font-size:8px;line-height:8px;color:var(--ink)}
.about-block h4{margin:1px 0 5px;font-size:12.5px;line-height:12px;font-weight:900;color:var(--red);letter-spacing:-.2px}

/* agenda */
.agenda{position:absolute;left:44px;top:44px;width:310px}
.day{position:relative;height:29px}
.day-no{position:absolute;left:0;top:0;width:30px;height:20px;background:var(--red);color:#fff;font-size:9px;line-height:20px;text-align:center}
.day:nth-child(even) .day-no{background:#a8a8a8}
.day-name{position:absolute;left:47px;top:-3px;font-size:6px;color:var(--ink)}
.day ul{position:absolute;top:4px;margin:0;padding:0 0 0 5px;font-size:3.8px;line-height:5px;color:var(--grey)}
.day ul li{margin:0}
.c1{left:55px}.c2{left:132px}.c3{left:210px}

/* introduction */
.intro-photo{left:0;top:55px;width:347px;height:100px}
.intro-panel{position:absolute;left:143px;top:55px;width:204px;height:100px;background:rgba(168,48,56,.88)}
.intro-panel .copy{position:absolute;left:50px;top:17px;width:140px;padding-left:4px;border-left:1px solid #fff;color:#fff}
.intro-panel h4{margin:0;font-size:15px;line-height:15px;font-weight:700}
.intro-panel h5{margin:1px 0 3px;font-size:8.5px;line-height:8.5px;font-weight:700}
.intro-panel p{margin:0;font-size:4.6px;line-height:6px;color:#f0d0d2}

.side-text{position:absolute;top:62px;width:150px}
.bullets3{position:absolute;left:34px;top:156px;width:320px;display:flex;justify-content:space-between;margin:0;padding:0;list-style:none}
.bullets3 ul{margin:0;padding-left:8px;font-size:5px;line-height:7px;color:var(--grey)}

/* factor list */
.factor{position:absolute;width:280px}
.factor .dot{position:absolute;left:0;top:1px;width:22px;height:22px;border-radius:50%;background:var(--red)}
.factor .dot::after{content:"";position:absolute;left:7px;top:7px;width:8px;height:8px;border-radius:50%;border:1.5px solid #fff}
.factor h6{margin:0 0 1px 29px;font-size:4.4px;font-weight:900;color:var(--ink)}
.factor p{margin:0 0 0 29px;font-size:3.8px;line-height:4.7px;color:var(--grey)}
.factor.small .dot{width:17px;height:17px}
.factor.small .dot::after{left:5px;top:5px;width:6px;height:6px}
.factor.small h6,.factor.small p{margin-left:24px}

/* icon topics */
.icon-topic{position:absolute;width:64px;text-align:center}
.icon-topic svg{display:block;margin:0 auto 3px}
.icon-topic h6{margin:0 0 2px;font-size:4.8px;font-weight:900;color:var(--ink)}
.icon-topic p{margin:0;font-size:3.7px;line-height:4.8px;color:var(--grey)}

/* two column text */
.cols{position:absolute;left:30px;top:44px;width:318px;display:flex;gap:12px}
.cols>div{flex:1}

/* process grid */
.cell{position:absolute}
.process-box{background:#9e9e9e;color:#fff;text-align:center}
.process-box h5{margin:13px 0 4px;font-size:10px;font-weight:700}
.process-box p{margin:0 14px;font-size:3.8px;line-height:4.7px;color:#e6e6e6}
.quote-box{background:var(--blue);color:#fff}
.quote-box .q{position:absolute;left:4px;top:4px;font-size:14px;line-height:14px;font-weight:900}
.quote-box p{position:absolute;left:14px;top:8px;width:54px;margin:0;font-size:3.8px;line-height:4.7px;color:#e9ecf6}

/* charts */
.chart-note{position:absolute;left:28px;top:54px;width:150px}
.chart-note h6{margin:0 0 3px;font-size:5px;font-weight:900;color:var(--ink)}
.chart-svg{position:absolute}
.chart-svg text{font-family:'Lato',sans-serif;font-size:5px;fill:var(--grey)}

/* infographic circles */
.bubble{position:absolute;width:90px;height:90px;border-radius:50%;color:#fff;text-align:center}
.bubble svg{display:block;margin:14px auto 4px}
.bubble h6{margin:0;font-size:5.5px;font-weight:400}
.bubble p{margin:0 16px;font-size:4.3px;line-height:5px}
.b1{background:var(--grey-light);left:18px;top:52px}
.b2{background:var(--pink);left:99px;top:52px;opacity:.97}
.b3{background:var(--grey-mid);left:180px;top:52px}
.b4{background:var(--red-bright);left:261px;top:52px}
.bottom-para{position:absolute;left:34px;width:300px}

/* comparison rings */
.element{position:absolute;width:80px;text-align:center}
.element svg{display:block;margin:0 auto}
.element h6{margin:8px 0 2px;font-size:4.4px;font-weight:900;color:var(--ink)}
.element p{margin:0;font-size:3.6px;line-height:4.5px;color:var(--grey)}

/* break */
.break-band{position:absolute;left:0;top:133px;width:100%;height:50px;background:rgba(168,38,47,.9)}
.break-band h4{position:absolute;left:32px;top:16px;margin:0;padding-left:6px;border-left:1.5px solid #fff;font-size:13px;line-height:16px;font-weight:700;color:#fff}
.mark.on-photo{top:10px}
</style>
</head>
<body>

<section class="hero" aria-label="Title slide">
  <div class="hero-photo" role="img" aria-label="Pumpjack silhouette against a pale washed-out sky"></div>
  <div class="hero-brand">
    <span class="name">RIDGEBORE</span>
    <span class="services">ENGINEERING • CONSULTING • TRAINING • EQUIPMENT</span>
  </div>
  <h1 class="hero-title">SOLIDS CONTROL AND<br>WASTE MANAGEMENT</h1>
</section>

<ul class="features">
  <li>Ratio 16:9</li>
  <li>Full HD</li>
  <li>Custom color pallet</li>
  <li>Custom Font - &nbsp;Easy Change</li>
  <li>Easy to edit, just drag and drop images</li>
  <li>Can be included up to 100 slides;
    <ul>
      <li>Text + images (1,2,3,4) , Text Slides</li>
      <li>Portfolio Slides , blog slides</li>
      <li>Text Slides, infographics</li>
      <li>Data Slides</li>
    </ul>
  </li>
  <li>In the sample you find 19 slides</li>
</ul>

<!-- row 1 -->
<article class="slide" style="left:20px;top:479px">
  <div class="head"><div class="mark"><b>RIDGEBORE</b><i>ENGINEERING • CONSULTING • TRAINING</i></div></div>
  <div class="photo ph-sky" style="left:25px;top:54px;width:150px;height:101px" role="img" aria-label="Two workers shaking hands beside a pumpjack at dusk"></div>
  <div class="about-block">
    <span class="kicker">About the Course</span>
    <h4>SOLIDS CONTROL AND WASTE MANAGEMENT</h4>
    <p class="txt">A five-day course on keeping drilling fluid clean, cutting waste volumes and handling cuttings safely from rig to disposal site.</p>
  </div>
  <div class="foot">SOLIDS CONTROL AND WASTE MANAGEMENT</div>
  <div class="page-no"><span>2</span></div>
</article>

<article class="slide" style="left:418px;top:479px">
  <div class="head"><h3 class="title">Agenda</h3><div class="mark"><b>RIDGEBORE</b><i>ENGINEERING • CONSULTING • TRAINING</i></div></div>
  <div class="agenda">
    <div class="day"><div class="day-no">01</div><div class="day-name">Day One</div>
      <ul class="c1"><li>• Rig layout and</li><li>&nbsp; flow of the fluid</li></ul><ul class="c2"><li>• Screen mesh and</li><li>&nbsp; cut point basics</li></ul><ul class="c3"><li>• Site visit and</li><li>&nbsp; daily wrap-up</li></ul></div>
    <div class="day"><div class="day-no">02</div><div class="day-name">Day Two</div>
      <ul class="c1"><li>• Rig layout and</li><li>&nbsp; flow of the fluid</li></ul><ul class="c2"><li>• Screen mesh and</li><li>&nbsp; cut point basics</li></ul><ul class="c3"><li>• Site visit and</li><li>&nbsp; daily wrap-up</li></ul></div>
    <div class="day"><div class="day-no">03</div><div class="day-name">Day Three</div>
      <ul class="c1"><li>• Rig layout and</li><li>&nbsp; flow of the fluid</li></ul><ul class="c2"><li>• Screen mesh and</li><li>&nbsp; cut point basics</li></ul><ul class="c3"><li>• Site visit and</li><li>&nbsp; daily wrap-up</li></ul></div>
    <div class="day"><div class="day-no">04</div><div class="day-name">Day Four</div>
      <ul class="c1"><li>• Rig layout and</li><li>&nbsp; flow of the fluid</li></ul><ul class="c2"><li>• Screen mesh and</li><li>&nbsp; cut point basics</li></ul><ul class="c3"><li>• Site visit and</li><li>&nbsp; daily wrap-up</li></ul></div>
    <div class="day"><div class="day-no">05</div><div class="day-name">Day Five</div>
      <ul class="c1"><li>• Rig layout and</li><li>&nbsp; flow of the fluid</li></ul><ul class="c2"><li>• Screen mesh and</li><li>&nbsp; cut point basics</li></ul><ul class="c3"><li>• Site visit and</li><li>&nbsp; daily wrap-up</li></ul></div>
  </div>
  <div class="foot">SOLIDS CONTROL AND WASTE MANAGEMENT</div>
  <div class="page-no"><span>3</span></div>
</article>

<article class="slide" style="left:816px;top:479px">
  <div class="head"><h3 class="title">Course <em>Overview</em></h3><div class="mark"><b>RIDGEBORE</b><i>ENGINEERING • CONSULTING • TRAINING</i></div></div>
  <div style="position:absolute;left:34px;top:46px;width:312px">
    <p class="txt">Solids control keeps drilling fluid in good shape by removing cuttings as they reach surface. Shakers take out coarse material, hydrocyclones handle sand and silt, and centrifuges recover barite or strip the finest solids before the mud returns to the pits.</p>
    <p class="txt">Waste management starts at the rig. Good separation means drier cuttings, less fluid lost and fewer loads to haul, which lowers cost and reduces the footprint of every well we drill.</p>
    <p class="txt">Each day mixes classroom time with hands-on work at the equipment, so crews leave able to set up, tune and troubleshoot a full system.</p>
  </div>
  <div class="foot">SOLIDS CONTROL AND WASTE MANAGEMENT</div>
  <div class="page-no"><span>4</span></div>
</article>

<!-- row 2 -->
<article class="slide" style="left:20px;top:765px">
  <div class="head"><div class="mark"><b>RIDGEBORE</b><i>ENGINEERING • CONSULTING • TRAINING</i></div></div>
  <div class="photo ph-plant intro-photo" role="img" aria-label="Green solids control tanks on a drilling site"></div>
  <div class="intro-panel">
    <div class="copy">
      <h4>Introduction</h4>
      <h5>SOLIDS CONTROL AND<br>WASTE MANAGEMENT</h5>
      <p>A practical week on solids control, from the shaker to final waste disposal.</p>
    </div>
  </div>
  <div class="foot">SOLIDS CONTROL AND WASTE MANAGEMENT</div>
  <div class="page-no"><span>5</span></div>
</article>

<article class="slide shaded" style="left:418px;top:765px">
  <div class="head"><h3 class="title">Topic <em>Number Two</em></h3><div class="mark"><b>RIDGEBORE</b><i>ENGINEERING • CONSULTING • TRAINING</i></div></div>
  <div class="side-text" style="left:32px"><p class="txt">Solids control keeps drilling fluid in good shape by removing cuttings as they reach surface. Shakers take out coarse material, hydrocyclones handle sand and silt, and centrifuges recover barite or strip the finest solids before the mud returns to the pits.</p></div>
  <div class="photo ph-plant" style="left:194px;top:54px;width:150px;height:101px" role="img" aria-label="Row of shale shakers mounted on mud tanks"></div>
  <div class="foot">SOLIDS CONTROL AND WASTE MANAGEMENT</div>
  <div class="page-no"><span>7</span></div>
</article>

<article class="slide shaded" style="left:816px;top:765px">
  <div class="head"><h3 class="title">Topic <em>Number One</em></h3><div class="mark"><b>RIDGEBORE</b><i>ENGINEERING • CONSULTING • TRAINING</i></div></div>
  <div class="photo ph-sunset" style="left:26px;top:54px;width:150px;height:101px" role="img" aria-label="Pumpjack silhouette under an amber sky"></div>
  <div class="side-text" style="left:194px"><p class="txt">Solids control keeps drilling fluid in good shape by removing cuttings as they reach surface. Shakers take out coarse material, hydrocyclones handle sand and silt, and centrifuges recover barite or strip the finest solids before the mud returns to the pits.</p></div>
  <div class="foot">SOLIDS CONTROL AND WASTE MANAGEMENT</div>
  <div class="page-no"><span>6</span></div>
</article>

<!-- row 3 -->
<article class="slide" style="left:20px;top:1051px">
  <div class="head"><h3 class="title">Topic <em>Number Four</em></h3><div class="mark"><b>RIDGEBORE</b><i>ENGINEERING • CONSULTING • TRAINING</i></div></div>
  <div class="photo ph-plant" style="left:0;top:50px;width:347px;height:102px" role="img" aria-label="Wide view of shakers and tanks on a rig site"></div>
  <div class="bullets3">
    <ul><li>Shaker screen choice</li><li>Flow line and gumbo</li><li>Feed to the cyclones</li></ul>
    <ul><li>Cut point of each unit</li><li>Weighted mud handling</li><li>Centrifuge speed set</li></ul>
    <ul><li>Dryer and cuttings box</li><li>Water treatment steps</li><li>Disposal and records</li></ul>
  </div>
  <div class="foot">SOLIDS CONTROL AND WASTE MANAGEMENT</div>
  <div class="page-no"><span>8</span></div>
</article>

<article class="slide" style="left:418px;top:1051px">
  <div class="head"><h3 class="title">Bulletpoint <em>Topics</em></h3><div class="mark"><b>RIDGEBORE</b><i>ENGINEERING • CONSULTING • TRAINING</i></div></div>
  <div class="factor" style="left:55px;top:59px"><span class="dot"></span><h6>Factor Number One</h6><p>Each day mixes classroom time with hands-on work at the equipment, so crews leave able to set up, tune and troubleshoot a full system.</p></div>
  <div class="factor" style="left:55px;top:92px"><span class="dot"></span><h6>Factor Number Two</h6><p>Each day mixes classroom time with hands-on work at the equipment, so crews leave able to set up, tune and troubleshoot a full system.</p></div>
  <div class="factor" style="left:55px;top:119px"><span class="dot"></span><h6>Factor Number Three</h6><p>Each day mixes classroom time with hands-on work at the equipment, so crews leave able to set up, tune and troubleshoot a full system.</p></div>
  <div class="factor" style="left:55px;top:153px"><span class="dot"></span><h6>Factor Number Four</h6><p>Each day mixes classroom time with hands-on work at the equipment, so crews leave able to set up, tune and troubleshoot a full system.</p></div>
  <div class="foot">SOLIDS CONTROL AND WASTE MANAGEMENT</div>
  <div class="page-no"><span>11</span></div>
</article>

<article class="slide" style="left:816px;top:1051px">
  <div class="head"><h3 class="title">Icon <em>Topics</em></h3><div class="mark"><b>RIDGEBORE</b><i>ENGINEERING • CONSULTING • TRAINING</i></div></div>
  <div class="icon-topic" style="left:45px;top:59px"><svg width="12" height="10" viewBox="0 0 12 10"><path d="M2 9 L3 6 L9 1 L11 3 L5 8 Z" fill="var(--red)"/></svg><h6>Graphic Design</h6><p>Short note on this topic, two lines.</p></div>
  <div class="icon-topic" style="left:116px;top:59px"><svg width="12" height="10" viewBox="0 0 12 10"><path d="M2 3.5h2.5L8 1v8L4.5 6.5H2z" fill="#9a9a9a"/></svg><h6>Sound Design</h6><p>Short note on this topic, two lines.</p></div>
  <div class="icon-topic" style="left:187px;top:59px"><svg width="12" height="10" viewBox="0 0 12 10"><rect x="1" y="3" width="10" height="6" rx="1" fill="#9a9a9a"/><rect x="4" y="1.5" width="4" height="2" fill="#9a9a9a"/><circle cx="6" cy="6" r="1.7" fill="#fff"/></svg><h6>Photography</h6><p>Short note on this topic, two lines.</p></div>
  <div class="icon-topic" style="left:259px;top:59px"><svg width="12" height="10" viewBox="0 0 12 10"><path d="M3 8.5h6.5a2 2 0 0 0 0-4A3 3 0 0 0 3.6 4 2.3 2.3 0 0 0 3 8.5z" fill="var(--blue)"/></svg><h6>Cloud Service</h6><p>Short note on this topic, two lines.</p></div>
  <div class="icon-topic" style="left:45px;top:117px"><svg width="12" height="10" viewBox="0 0 12 10"><rect x="1" y="2.5" width="7" height="5" fill="var(--red)"/><path d="M8 5 11 3v4z" fill="var(--red)"/></svg><h6>Tv Production</h6><p>Short note on this topic, two lines.</p></div>
  <div class="icon-topic" style="left:116px;top:117px"><svg width="12" height="10" viewBox="0 0 12 10"><path d="M4.5 1h3M5 1v3L2 9h8L7 4V1" fill="none" stroke="var(--red)" stroke-width="1.2"/></svg><h6>Research</h6><p>Short note on this topic, two lines.</p></div>
  <div class="icon-topic" style="left:187px;top:117px"><svg width="12" height="10" viewBox="0 0 12 10"><path d="M2 4h2l6-3v8L4 6H2z" fill="var(--red)"/></svg><h6>Marketing</h6><p>Short note on this topic, two lines.</p></div>
  <div class="icon-topic" style="left:259px;top:117px"><svg width="12" height="10" viewBox="0 0 12 10"><rect x="1.5" y="1.5" width="9" height="7" fill="none" stroke="#9a9a9a"/><path d="M2.5 7.5 5 5l2 2 1.5-1.5 1.5 2z" fill="#9a9a9a"/></svg><h6>Pictures</h6><p>Short note on this topic, two lines.</p></div>
  <div class="foot">SOLIDS CONTROL AND WASTE MANAGEMENT</div>
  <div class="page-no"><span>10</span></div>
</article>

<!-- row 4 -->
<article class="slide" style="left:20px;top:1337px">
  <div class="head"><h3 class="title">Talk about <em>Text</em> <em>Topic</em></h3><div class="mark"><b>RIDGEBORE</b><i>ENGINEERING • CONSULTING • TRAINING</i></div></div>
  <div class="cols">
    <div>
      <p class="txt">Solids control keeps drilling fluid in good shape by removing cuttings as they reach surface. Shakers take out coarse material, hydrocyclones handle sand and silt, and centrifuges recover barite or strip the finest solids before the mud returns to the pits.</p>
      <p class="txt">Waste management starts at the rig. Good separation means drier cuttings, less fluid lost and fewer loads to haul, which lowers cost and reduces the footprint of every well we drill.</p>
    </div>
    <div>
      <p class="txt">Waste management starts at the rig. Good separation means drier cuttings, less fluid lost and fewer loads to haul, which lowers cost and reduces the footprint of every well we drill.</p>
      <p class="txt">Solids control keeps drilling fluid in good shape by removing cuttings as they reach surface. Shakers take out coarse material, hydrocyclones handle sand and silt, and centrifuges recover barite or strip the finest solids before the mud returns to the pits.</p>
    </div>
  </div>
  <div class="foot">SOLIDS CONTROL AND WASTE MANAGEMENT</div>
  <div class="page-no"><span>12</span></div>
</article>

<article class="slide" style="left:418px;top:1337px">
  <div class="head"><h3 class="title">Topic <em>Number</em></h3><div class="mark"><b>RIDGEBORE</b><i>ENGINEERING • CONSULTING • TRAINING</i></div></div>
  <div style="position:absolute;left:32px;top:42px;width:312px">
    <p class="txt">Solids control keeps drilling fluid in good shape by removing cuttings as they reach surface. Shakers take out coarse material, hydrocyclones handle sand and silt, and centrifuges recover barite or strip the finest solids before the mud returns to the pits.</p>
    <p class="txt">Waste management starts at the rig. Good separation means drier cuttings, less fluid lost and fewer loads to haul, which lowers cost and reduces the footprint of every well we drill.</p>
  </div>
  <div class="photo ph-screen" style="left:27px;top:113px;width:102px;height:84px" role="img" aria-label="Close view of cuttings on a shaker screen"></div>
  <div class="photo ph-crew" style="left:136px;top:113px;width:102px;height:84px" role="img" aria-label="Worker in coveralls checking a screen panel"></div>
  <div class="photo ph-pit" style="left:245px;top:113px;width:102px;height:84px" role="img" aria-label="Fluid flowing through a reserve pit"></div>
  <div class="page-no"><span>15</span></div>
</article>

<article class="slide" style="left:816px;top:1337px">
  <div class="head"><h3 class="title">The Process <em>We talk about</em></h3><div class="mark"><b>RIDGEBORE</b><i>ENGINEERING • CONSULTING • TRAINING</i></div></div>
  <div class="cell process-box" style="left:0;top:46px;width:154px;height:64px"><h5>Process Steps</h5><p>Each day mixes classroom time with hands-on work at the equipment, so crews leave able to set up, tune and troubleshoot a full system.</p></div>
  <div class="cell photo ph-sunset" style="left:154px;top:46px;width:74px;height:64px" role="img" aria-label="Pumpjack at sunset"></div>
  <div class="cell photo ph-plant" style="left:228px;top:46px;width:73px;height:64px" role="img" aria-label="Shakers on a mud tank"></div>
  <div class="cell photo ph-screen" style="left:301px;top:46px;width:69px;height:64px" role="img" aria-label="Wet cuttings on a screen"></div>
  <div class="cell" style="left:0;top:110px;width:82px;height:70px;background:#3c3c3c"></div>
  <div class="cell photo ph-crew" style="left:82px;top:110px;width:72px;height:70px" role="img" aria-label="Worker handling a screen panel"></div>
  <div class="cell photo ph-pit" style="left:154px;top:110px;width:74px;height:70px" role="img" aria-label="Flooded pit on a well site"></div>
  <div class="cell quote-box" style="left:228px;top:110px;width:73px;height:70px"><span class="q">“</span><p>A practical week on solids control, from the shaker to final waste disposal.</p></div>
  <div class="cell photo ph-sky" style="left:301px;top:110px;width:69px;height:70px" role="img" aria-label="Two workers beside a pumpjack at dusk"></div>
  <div class="foot">SOLIDS CONTROL AND WASTE MANAGEMENT</div>
  <div class="page-no"><span>16</span></div>
</article>

<!-- row 5 -->
<article class="slide" style="left:20px;top:1623px">
  <div class="head"><h3 class="title">Text <em>and Bullets</em></h3><div class="mark"><b>RIDGEBORE</b><i>ENGINEERING • CONSULTING • TRAINING</i></div></div>
  <div style="position:absolute;left:30px;top:40px;width:318px">
    <p class="txt">Solids control keeps drilling fluid in good shape by removing cuttings as they reach surface. Shakers take out coarse material, hydrocyclones handle sand and silt, and centrifuges recover barite or strip the finest solids before the mud returns to the pits.</p>
    <p class="txt" style="margin-top:2px">Waste management starts at the rig. Good separation means drier cuttings, less fluid lost and fewer loads to haul, which lowers cost and reduces the footprint of every well we drill.</p>
  </div>
  <div class="factor small" style="left:107px;top:109px;width:220px"><span class="dot"></span><h6>Factor Number One</h6><p>Short note on this point, kept to two lines of text.</p></div>
  <div class="factor small" style="left:107px;top:140px;width:220px"><span class="dot"></span><h6>Factor Number Two</h6><p>Short note on this point, kept to two lines of text.</p></div>
  <div class="factor small" style="left:107px;top:168px;width:220px"><span class="dot"></span><h6>Factor Number Three</h6><p>Short note on this point, kept to two lines of text.</p></div>
  <div class="foot">SOLIDS CONTROL AND WASTE MANAGEMENT</div>
  <div class="page-no"><span>13</span></div>
</article>

<article class="slide" style="left:418px;top:1623px">
  <div class="head"><h3 class="title">Analytics <em>Three Facts</em></h3><div class="mark"><b>RIDGEBORE</b><i>ENGINEERING • CONSULTING • TRAINING</i></div></div>
  <div class="chart-note"><h6>Analysis of the Chart</h6><p class="txt">Solids control keeps drilling fluid in good shape by removing cuttings as they reach surface. Shakers take out coarse material, hydrocyclones handle sand and silt, and centrifuges recover barite or strip the finest solids before the mud returns to the pits.</p></div>
  <svg class="chart-svg" style="left:186px;top:58px" width="160" height="100" viewBox="0 0 160 100" role="img" aria-label="Area chart of two series across four categories">
    <g text-anchor="end"><text x="8" y="87">0</text><text x="8" y="74">1</text><text x="8" y="61">2</text><text x="8" y="47">3</text><text x="8" y="34">4</text><text x="8" y="21">5</text><text x="8" y="7">6</text></g>
    <path d="M14 85 L14 27.7 L58 50.3 L102 39.7 L146 23.7 L146 85 Z" fill="var(--red)"/>
    <path d="M14 85 L14 50.3 L58 37 L102 21 L146 29 L146 85 Z" fill="#c4c4c4"/>
    <line x1="14" y1="85" x2="146" y2="85" stroke="#cfcfcf" stroke-width=".5"/>
    <g text-anchor="middle"><text x="20" y="96">Category 1</text><text x="58" y="96">Category 2</text><text x="102" y="96">Category 3</text><text x="142" y="96">Category 4</text></g>
  </svg>
  <div class="foot">SOLIDS CONTROL AND WASTE MANAGEMENT</div>
  <div class="page-no"><span>18</span></div>
</article>

<article class="slide" style="left:816px;top:1623px">
  <div class="head"><h3 class="title">Analytics <em>Three Facts</em></h3><div class="mark"><b>RIDGEBORE</b><i>ENGINEERING • CONSULTING • TRAINING</i></div></div>
  <svg class="chart-svg" style="left:30px;top:66px" width="160" height="90" viewBox="0 0 160 90" role="img" aria-label="Stacked bar chart for four categories">
    <g text-anchor="end"><text x="37" y="11">Category 4</text><text x="37" y="30">Category 3</text><text x="37" y="49">Category 2</text><text x="37" y="68">Category 1</text></g>
    <g>
      <rect x="40" y="6" width="106" height="7" fill="#e3e3e3"/><rect x="40" y="6" width="40" height="7" fill="var(--red)"/><rect x="80" y="6" width="24" height="7" fill="#c8c8c8"/>
      <rect x="40" y="25" width="106" height="7" fill="#e3e3e3"/><rect x="40" y="25" width="46" height="7" fill="var(--red)"/><rect x="86" y="25" width="24" height="7" fill="#c8c8c8"/>
      <rect x="40" y="44" width="106" height="7" fill="#e3e3e3"/><rect x="40" y="44" width="32" height="7" fill="var(--red)"/><rect x="72" y="44" width="30" height="7" fill="#c8c8c8"/>
      <rect x="40" y="63" width="106" height="7" fill="#e3e3e3"/><rect x="40" y="63" width="40" height="7" fill="var(--red)"/><rect x="80" y="63" width="22" height="7" fill="#c8c8c8"/>
    </g>
    <g text-anchor="middle"><text x="40" y="84">0%</text><text x="61" y="84">20%</text><text x="82" y="84">40%</text><text x="104" y="84">60%</text><text x="125" y="84">80%</text><text x="146" y="84">100%</text></g>
  </svg>
  <div class="factor small" style="left:206px;top:70px;width:140px"><span class="dot"></span><h6>Factor Number One</h6><p>Short note on this point, kept to two lines of text.</p></div>
  <div class="factor small" style="left:206px;top:101px;width:140px"><span class="dot" style="background:#9a9a9a"></span><h6>Factor Number Two</h6><p>Short note on this point, kept to two lines of text.</p></div>
  <div class="factor small" style="left:206px;top:129px;width:140px"><span class="dot" style="background:#bdbdbd"></span><h6>Factor Number Three</h6><p>Short note on this point, kept to two lines of text.</p></div>
  <div class="foot">SOLIDS CONTROL AND WASTE MANAGEMENT</div>
  <div class="page-no"><span>17</span></div>
</article>

<!-- row 6 -->
<article class="slide" style="left:20px;top:1909px">
  <div class="head"><h3 class="title">Infographic <em>Slides</em></h3><div class="mark"><b>RIDGEBORE</b><i>ENGINEERING • CONSULTING • TRAINING</i></div></div>
  <div class="bubble b1"><svg width="18" height="14" viewBox="0 0 18 14"><rect x="1" y="3" width="16" height="10" rx="1.5" fill="none" stroke="#fff" stroke-width="1.3"/><circle cx="9" cy="8" r="3" fill="none" stroke="#fff" stroke-width="1.3"/></svg><h6>Photography</h6><p>Short note here in three short lines</p></div>
  <div class="bubble b2"><svg width="18" height="14" viewBox="0 0 18 14"><rect x="1" y="1" width="16" height="12" fill="none" stroke="#fff" stroke-width="1.3"/><path d="M9 10V4M6 7l3-3 3 3" fill="none" stroke="#fff" stroke-width="1.3"/></svg><h6>Web Server</h6><p>Short note here in three short lines</p></div>
  <div class="bubble b3"><svg width="18" height="14" viewBox="0 0 18 14"><path d="M3 13 13 3M5 3l10 10" stroke="#fff" stroke-width="2"/></svg><h6>Web Design</h6><p>Short note here in three short lines</p></div>
  <div class="bubble b4"><svg width="18" height="14" viewBox="0 0 18 14"><path d="M2 5h3l9-4v12L5 9H2z" fill="#fff"/></svg><h6>Promotion</h6><p>Short note here in three short lines</p></div>
  <p class="txt bottom-para" style="top:157px">Waste management starts at the rig. Good separation means drier cuttings, less fluid lost and fewer loads to haul, which lowers cost and reduces the footprint of every well we drill.</p>
  <div class="foot">SOLIDS CONTROL AND WASTE MANAGEMENT</div>
  <div class="page-no"><span>19</span></div>
</article>

<article class="slide" style="left:418px;top:1909px">
  <div class="head"><h3 class="title">Elements <em>Comparison Chart</em></h3><div class="mark"><b>RIDGEBORE</b><i>ENGINEERING • CONSULTING • TRAINING</i></div></div>
  <div class="element" style="left:24px;top:57px"><svg width="64" height="64" viewBox="0 0 64 64"><path d="M32 2A30 30 0 0 0 32 62" fill="none" stroke="var(--red)" stroke-width="2"/><path d="M32 2A30 30 0 0 1 32 62" fill="none" stroke="var(--blue)" stroke-width="2"/><circle cx="32" cy="32" r="6" fill="var(--red)"/></svg><h6>ELEMENT ONE</h6><p>Short note on this element here</p></div>
  <div class="element" style="left:103px;top:57px"><svg width="64" height="64" viewBox="0 0 64 64"><path d="M32 2A30 30 0 0 0 32 62" fill="none" stroke="var(--red)" stroke-width="2"/><path d="M32 2A30 30 0 0 1 32 62" fill="none" stroke="var(--blue)" stroke-width="2"/><circle cx="32" cy="32" r="6" fill="#b5b5b5"/></svg><h6>ELEMENT TWO</h6><p>Short note on this element here</p></div>
  <div class="element" style="left:191px;top:57px"><svg width="64" height="64" viewBox="0 0 64 64"><path d="M32 2A30 30 0 0 0 32 62" fill="none" stroke="var(--red)" stroke-width="2"/><path d="M32 2A30 30 0 0 1 32 62" fill="none" stroke="var(--blue)" stroke-width="2"/><circle cx="32" cy="32" r="6" fill="#b5b5b5"/></svg><h6>ELEMENT THREE</h6><p>Short note on this element here</p></div>
  <div class="element" style="left:271px;top:57px"><svg width="64" height="64" viewBox="0 0 64 64"><path d="M32 2A30 30 0 0 0 32 62" fill="none" stroke="var(--red)" stroke-width="2"/><path d="M32 2A30 30 0 0 1 32 62" fill="none" stroke="var(--blue)" stroke-width="2"/><rect x="26" y="26" width="12" height="12" fill="var(--blue)"/></svg><h6>ELEMENT FOUR</h6><p>Short note on this element here</p></div>
  <p class="txt bottom-para" style="top:163px">Waste management starts at the rig. Good separation means drier cuttings, less fluid lost and fewer loads to haul, which lowers cost and reduces the footprint of every well we drill.</p>
  <div class="foot">SOLIDS CONTROL AND WASTE MANAGEMENT</div>
  <div class="page-no"><span>20</span></div>
</article>

<article class="slide" style="left:816px;top:1909px">
  <div class="photo ph-tower" style="inset:0" role="img" aria-label="Faded drilling rig derrick in grey"></div>
  <div class="mark on-photo"><b>RIDGEBORE</b><i>ENGINEERING • CONSULTING • TRAINING</i></div>
  <div class="break-band"><h4>Break Time</h4></div>
</article>

</body>
</html>
```